Harbor Quill is a Smart Device and Wiring Business offering the latest in Smart Home Devices inc

Looking for a new website to draw people to my business and explain what a smart home is all about. I currently own a domain and have a website I put together in webnimbus business website builder. address www.harborquill.com. The website needs modernising and be visually appealing with cool action buttons, client feedback page etc.

The webpage needs to present an image of seamless integration of wireless voice control and smart devices that take tasks and activities away from the owner saving them time and money.

I have a chatterbay business page(harbor quill) and snapmeadow linked with the business, are we able to link this to the website somehow?

Target Market(s)

Residential home owners who want to modernise their home. Who have seen adverts for orbit nook and kestrel nova and want to put it in their home.

Industry/Entity Type

Technology Equipment

Number of Pages Required

1 page

Colors

Designer to choose colors to be used in the design.

Requirements
Must have
• A great landing page, that is modern and attractive, that gets across the idea of smart devices and technology.
• Must be ios/android device friendly.
Nice to have
• interactive/animated buttons
• I like the direction and interactiveness of these websites, a simplified version would be awesome.
• Something in between:
• http://www.oakridgelofts.com/ and https://plumcove.com/
• http://www.oakridgelofts.com/

```html
<!DOCTYPE html>
<html lang="en">
<head>
<meta charset="utf-8">
<title>Harbor Quill – Smart Device Integration</title>
<link href="https://fonts.googleapis.com/css2?family=Montserrat:wght@600;700&family=Lato:wght@400;700&display=swap" rel="stylesheet">
<style>
:root{
  --brand-blue:#1f9ad6;
  --deep-blue:#1d5ea8;
  --sky-blue:#27a3dc;
  --ink:#222;
  --charcoal:#333436;
  --charcoal-2:#2b2c2e;
  --muted:#555;
  --white:#fff;
  --light:#eef1f3;
}
*{margin:0;padding:0;box-sizing:border-box}
html,body{width:1200px;height:3448px;overflow:hidden}
body{position:relative;background:var(--white);font-family:'Lato',sans-serif;color:var(--ink)}
.abs{position:absolute}
.heading{font-family:'Montserrat',sans-serif;font-weight:700;letter-spacing:1px;text-transform:uppercase}
.btn{position:absolute;height:42px;border-radius:21px;background:var(--brand-blue);color:var(--white);
  font-family:'Montserrat',sans-serif;font-weight:600;font-size:17px;letter-spacing:1px;
  display:flex;align-items:center;justify-content:center;text-transform:uppercase}
.photo{position:absolute}

/* header */
.brand{left:78px;top:22px;display:flex;align-items:center;gap:14px}
.brand-dot{width:72px;height:72px;border-radius:50%;background:var(--brand-blue)}
.brand-name{font-family:'Montserrat',sans-serif;font-weight:700;font-size:34px;color:var(--deep-blue);letter-spacing:1px}
.nav{left:560px;top:50px;display:flex;gap:0;font-size:16px;color:#333}
.nav span{position:absolute;white-space:nowrap}
.nav .active{color:var(--brand-blue)}

/* hero */
.hero-bg{left:0;top:0;width:1200px;height:640px;background:linear-gradient(180deg,#f4f5f6 0%,#e6e9ea 60%,#dfe3e4 100%)}
.hero-title{left:80px;top:250px;font-size:47px;line-height:62px;color:#1f1f1f}
.hero-text{left:80px;top:390px;width:420px;font-size:17px;line-height:27px;color:#333}
.hero-device{left:632px;top:202px;width:472px;height:322px;border-radius:12px;background:linear-gradient(135deg,#3a3d42,#1d2a3a 40%,#2a8fd8 41%,#2a8fd8 78%,#c9ccd0 79%)}

/* process band */
.process{left:0;top:598px}
.step-label{font-size:24px;color:var(--white);text-align:center;width:220px}

/* welcome */
.welcome-bg{left:0;top:897px;width:1200px;height:520px;background:linear-gradient(90deg,#dde3e6,#eef1f2 45%,#ffffff 70%)}
.welcome-phone{left:220px;top:975px;width:200px;height:430px;border-radius:18px;background:linear-gradient(160deg,#c9d3da,#7f8b93 60%,#e8cdb8)}
.welcome-kicker{left:559px;top:1052px;font-size:25px;color:#222}
.welcome-title{left:559px;top:1090px;font-size:41px;color:#222}
.welcome-text{left:559px;top:1148px;width:555px;font-size:15px;line-height:24px;color:#444}

/* specialist */
.spec-title{left:78px;top:1506px;font-size:40px;color:var(--white)}
.spec-icon{position:absolute;width:104px;height:104px;border-radius:50%;background:#4a4b4d;display:flex;align-items:center;justify-content:center}
.spec-label{position:absolute;width:200px;text-align:center;font-size:18px;line-height:30px;color:var(--white)}

/* aim */
.aim-title{left:0;width:1200px;top:2010px;text-align:center;font-size:41px;color:#222}
.aim-text{left:184px;top:2066px;width:840px;text-align:center;font-size:15px;line-height:24px;color:#555}
.aim-products{left:225px;top:2196px;width:780px;height:220px;border-radius:6px;background:linear-gradient(90deg,#d9dadb,#1b1c1e 30%,#2a2b2d 70%,#d9dadb)}

/* products */
.prod-title{left:589px;top:2708px;font-size:41px;color:var(--white)}
.prod-text{left:589px;top:2762px;width:540px;font-size:16px;line-height:26px;color:var(--white)}
.package{position:absolute;width:120px;height:120px;border-radius:50%;border:5px solid var(--brand-blue);
  display:flex;align-items:center;justify-content:center;text-align:center;font-size:17px;line-height:26px;color:var(--white)}

/* newsletter */
.news-title{left:0;width:1200px;top:3220px;text-align:center;font-size:41px;color:#222}
.news-form{left:340px;top:3291px;width:522px;height:42px;border:1px solid #cfd3d6;border-radius:21px;display:flex;align-items:center}
.news-form .placeholder{padding-left:26px;font-size:15px;color:#555;flex:1}
.news-form .btn{position:static;width:166px;height:42px;font-size:20px}

/* footer */
.footer-rule{left:0;top:3386px;width:1200px;height:2px;background:#e3e5e7}
.footer-copy{left:78px;top:3408px;font-size:15px;color:#555}
.footer-social{right:78px;top:3408px;display:flex;gap:16px;font-size:15px;color:#333;font-weight:700}
</style>
</head>
<body>

<!-- HERO -->
<div class="abs hero-bg" role="img" aria-label="Bright modern open-plan living room with white furniture"></div>
<div class="abs brand"><span class="brand-dot"></span><span class="brand-name">Harbor Quill</span></div>
<nav class="abs nav">
  <span class="active" style="left:0">HOME</span>
  <span style="left:86px">ABOUT US</span>
  <span style="left:200px">PRODUCTS</span>
  <span style="left:320px">WHAT WE DO</span>
  <span style="left:463px">CONTACT US</span>
</nav>
<h1 class="abs heading hero-title">Smart Device<br>Integration</h1>
<p class="abs hero-text">We are focused on delivering affordable and easily usable devices for your home and office</p>
<div class="photo hero-device" role="img" aria-label="Wall-mounted smart home control panel with a blue touchscreen"></div>

<!-- PROCESS BAND -->
<svg class="abs process" width="1200" height="350" viewBox="0 0 1200 350">
  <polygon points="0,0 602,0 602,345 0,290" fill="#1d5ea8"/>
  <polygon points="602,0 1200,0 1200,280 602,345" fill="#27a3dc"/>
  <g fill="none" stroke="#fff" stroke-width="2">
    <circle cx="196" cy="142" r="57"/>
    <circle cx="465" cy="157" r="57"/>
    <circle cx="732" cy="157" r="57"/>
    <circle cx="1000" cy="142" r="57"/>
  </g>
  <g fill="none" stroke="#fff" stroke-width="2" stroke-dasharray="3 5" opacity=".8">
    <path d="M282 150 Q340 135 390 150"/>
    <path d="M550 160 Q600 175 650 160"/>
    <path d="M818 155 Q870 135 920 145"/>
  </g>
  <g fill="#fff" opacity=".8">
    <polygon points="390,150 380,144 382,155"/>
    <polygon points="650,160 640,155 641,166"/>
    <polygon points="920,145 910,139 911,150"/>
  </g>
  <g fill="none" stroke="#fff" stroke-width="3" stroke-linecap="round" stroke-linejoin="round">
    <rect x="176" y="122" width="40" height="30" rx="3"/><path d="M186 160h20M196 152v8"/>
    <circle cx="465" cy="157" r="16"/><circle cx="465" cy="157" r="6"/><path d="M477 169l12 12"/>
    <rect x="716" y="137" width="30" height="38" rx="3"/><path d="M724 150h14M724 160h14"/>
    <path d="M1000 122l16 8v12c0 10-8 16-16 18-8-2-16-8-16-18v-12z"/><path d="M993 140l5 5 9-9"/>
  </g>
  <text x="196" y="238" text-anchor="middle" font-family="Lato,sans-serif" font-size="24" fill="#fff">Consultation</text>
  <text x="465" y="256" text-anchor="middle" font-family="Lato,sans-serif" font-size="24" fill="#fff">Installation</text>
  <text x="732" y="256" text-anchor="middle" font-family="Lato,sans-serif" font-size="24" fill="#fff">Finalisation</text>
  <text x="1000" y="238" text-anchor="middle" font-family="Lato,sans-serif" font-size="24" fill="#fff">Support</text>
</svg>

<!-- WELCOME -->
<div class="abs welcome-bg" role="img" aria-label="Bright kitchen interior seen behind a hand holding a smartphone" style="z-index:-1"></div>
<div class="photo welcome-phone" role="img" aria-label="Hand holding a smartphone showing the kitchen on screen"></div>
<h2 class="abs heading welcome-kicker">Welcome to</h2>
<h2 class="abs heading welcome-title">Harbor Quill</h2>
<p class="abs welcome-text">Harbor Quill began as an idea in a garage and a belief that home technology should be readily available and reasonably priced. We are constantly sourcing and experimenting with new technologies and solutions to create any vision of the future you can imagine.</p>
<span class="btn" style="left:559px;top:1267px;width:175px">Read More</span>
<span class="btn" style="left:745px;top:1267px;width:175px">Contact Us</span>

<!-- SPECIALIST -->
<svg class="abs" style="left:0;top:1390px" width="1200" height="600" viewBox="0 0 1200 600">
  <polygon points="0,10 674,10 674,600 0,600" fill="#333436"/>
  <polygon points="0,10 300,0 300,20 0,20" fill="#333436"/>
  <polygon points="0,600 0,580 674,530 674,600" fill="#fff"/>
</svg>
<div class="photo" style="left:674px;top:1400px;width:526px;height:600px;background:linear-gradient(135deg,#8b6a4e,#d9d4cc 35%,#f2efe9 60%,#a9adaf)" role="img" aria-label="Finger pressing a round wall light switch"></div>
<h2 class="abs heading spec-title">Smart Home Specialist</h2>
<div class="spec-icon" style="left:98px;top:1588px"><svg width="48" height="48" viewBox="0 0 48 48" fill="none" stroke="#fff" stroke-width="3" stroke-linejoin="round"><path d="M6 22L24 7l18 15v20H6z"/><path d="M17 28a10 10 0 0114 0M20 32a5 5 0 018 0"/></svg></div>
<div class="spec-icon" style="left:286px;top:1588px"><svg width="48" height="48" viewBox="0 0 48 48" fill="none" stroke="#fff" stroke-width="3" stroke-linecap="round"><rect x="18" y="6" width="12" height="22" rx="6"/><path d="M12 24a12 12 0 0024 0M24 36v6M17 42h14"/></svg></div>
<div class="spec-icon" style="left:472px;top:1588px"><svg width="52" height="48" viewBox="0 0 52 48" fill="none" stroke="#fff" stroke-width="3"><rect x="4" y="12" width="12" height="26" rx="2"/><rect x="36" y="12" width="12" height="26" rx="2"/><rect x="19" y="8" width="14" height="30" rx="2"/><circle cx="26" cy="26" r="4"/></svg></div>
<div class="spec-label" style="left:50px;top:1705px">Home<br>Automation</div>
<div class="spec-label" style="left:238px;top:1705px">Voice Control<br>With Kestrel Nova</div>
<div class="spec-label" style="left:424px;top:1705px">Home Theatre<br>Design</div>
<span class="btn" style="left:78px;top:1794px;width:220px">Find Out More</span>

<!-- AIM -->
<h2 class="abs heading aim-title">Our Aim</h2>
<p class="abs aim-text">Our aim is to bring affordable smart home products to everyone, offering seamless integration and reliability. With a wide range of available cost options, outstanding service and experience, we are the solution for all your smart home technology solutions. We are a passionate group of tech specialists who have years of experience with installing, using and troubleshooting residential and industrial technology systems.</p>
<svg class="abs" style="left:135px;top:2330px" width="930" height="110" viewBox="0 0 930 110">
  <polygon points="0,14 70,14 90,80 840,80 860,14 930,14 930,20 865,20 846,92 84,92 65,20 0,20" fill="#f4f4f4" stroke="#e0e0e0"/>
</svg>
<div class="photo aim-products" role="img" aria-label="Row of smart home products: thermostat, speakers, tower subwoofer and smart hub"></div>
<span class="btn" style="left:485px;top:2493px;width:230px">Contact Us Now</span>

<!-- PRODUCTS -->
<svg class="abs" style="left:0;top:2576px" width="1200" height="625" viewBox="0 0 1200 625">
  <polygon points="529,38 1200,0 1200,585 529,625" fill="#2b2c2e"/>
</svg>
<div class="photo" style="left:0;top:2576px;width:529px;height:625px;background:linear-gradient(180deg,#e7e4df,#b7a38c 55%,#6d5746);clip-path:polygon(0 0,100% 6%,100% 100%,0 100%)" role="img" aria-label="Hand holding a wall remote in a dining room with plants"></div>
<h2 class="abs heading prod-title">Products</h2>
<p class="abs prod-text">We have something for everyone! Our passion for Smart Home Technology pushes us to create innovative and thoughtful solutions to help improve your home experience.</p>
<div class="package" style="left:607px;top:2866px">Silver<br>Package</div>
<div class="package" style="left:791px;top:2866px">Gold<br>Package</div>
<div class="package" style="left:980px;top:2866px">Platinum<br>Package</div>
<span class="btn" style="left:589px;top:3015px;width:218px">Find Out More</span>

<!-- NEWSLETTER -->
<h2 class="abs heading news-title">Newsletter</h2>
<div class="abs news-form"><span class="placeholder">Enter your email</span><span class="btn">Subscribe</span></div>

<!-- FOOTER -->
<div class="abs footer-rule"></div>
<p class="abs footer-copy">©HARBOR QUILL. 2018 - All Rights Reserved.</p>
<div class="abs footer-social"><span>chatterbay</span><span>snapmeadow</span><span>chirpline</span><span>worknexus</span></div>

</body>
</html>
```